Maple Lantern Business Card

Design of business cards

Target Market(s)

We are aiming as small business owners who need anything from basic business structures, website plans, business processes and quality assurance.

Industry/Entity Type

Business

Colors

Designer to choose colors to be used in the design.

Requirements
Nice to have
• I would prefer one side of the card to use the green from the logo. Prefer to have the same font as the logo.

```html
<!DOCTYPE html>
<html lang="en">
<head>
<meta charset="utf-8">
<title>Maple Lantern Consulting – Business Card</title>
<link rel="stylesheet" href="https://fonts.googleapis.com/css2?family=Cinzel:wght@500&family=Tinos:wght@700&display=swap">
<style>
  :root {
    --lime: #9dcb2b;
    --lime-soft: #b2d85a;
    --charcoal: #3e3f36;
    --paper: #f4f4f4;
    --paper-shade: #e2e2e2;
    --ink: #1e1e1e;
    --backdrop: #e9e9e9;
  }
  * { margin: 0; padding: 0; box-sizing: border-box; }
  html, body { width: 1200px; height: 1200px; overflow: hidden; }
  body {
    background: var(--backdrop);
    display: flex;
    flex-direction: column;
    align-items: center;
    justify-content: center;
    gap: 60px;
  }
  .card {
    position: relative;
    width: 700px;
    height: 400px;
    overflow: hidden;
    box-shadow: 0 6px 18px rgba(0,0,0,0.12);
  }
  /* Front */
  .card-front {
    background: var(--lime);
    display: flex;
    align-items: center;
    justify-content: center;
  }
  .front-pattern {
    position: absolute;
    inset: 0;
    background: linear-gradient(135deg, var(--lime-soft), var(--lime) 60%);
  }
  .front-name {
    position: relative;
    font-family: "Cinzel", serif;
    font-weight: 500;
    font-size: 38px;
    color: #ffffff;
    letter-spacing: 2px;
    text-align: center;
    line-height: 1.2;
  }
  /* Back */
  .card-back {
    background: linear-gradient(160deg, #ffffff 0%, var(--paper) 55%, var(--paper-shade) 100%);
  }
  .back-bands { position: absolute; inset: 0; }
  .back-brand {
    position: absolute;
    top: 70px;
    left: 250px;
    display: flex;
    align-items: center;
    gap: 14px;
  }
  .brand-dot {
    width: 22px; height: 22px;
    border-radius: 50%;
    background: var(--lime);
  }
  .brand-name {
    font-family: "Cinzel", serif;
    font-weight: 500;
    font-size: 30px;
    color: var(--charcoal);
    letter-spacing: 2px;
    line-height: 1.15;
  }
  .holder-name {
    position: absolute;
    top: 210px;
    left: 40px;
    font-family: "Tinos", serif;
    font-weight: 700;
    font-size: 20px;
    color: var(--ink);
  }
  .contact {
    position: absolute;
    top: 292px;
    right: 34px;
    display: flex;
    align-items: center;
    gap: 12px;
    font-family: "Tinos", serif;
    font-weight: 700;
    font-size: 15px;
    color: var(--ink);
  }
</style>
</head>
<body>
  <section class="card card-front" aria-label="Business card front">
    <div class="front-pattern" role="img" aria-label="Repeating monogram pattern on green background"></div>
    <p class="front-name">Maple Lantern<br>Consulting</p>
  </section>

  <section class="card card-back" aria-label="Business card back">
    <svg class="back-bands" width="700" height="400" viewBox="0 0 700 400" aria-hidden="true">
      <polygon points="0,160 330,160 390,400 0,400" fill="var(--lime)"/>
      <polygon points="370,330 700,330 700,400 388,400" fill="var(--charcoal)"/>
    </svg>
    <div class="back-brand">
      <span class="brand-dot"></span>
      <p class="brand-name">Maple Lantern<br>Consulting</p>
    </div>
    <p class="holder-name">Name : xxxx xxx</p>
    <div class="contact">
      <span>xxx xxx-xxxx</span>
      <svg width="26" height="26" viewBox="0 0 26 26" aria-label="Phone">
        <circle cx="13" cy="13" r="13" fill="var(--ink)"/>
        <rect x="9" y="6" width="8" height="14" rx="1.5" fill="none" stroke="#fff" stroke-width="1.5"/>
        <line x1="11" y1="17.5" x2="15" y2="17.5" stroke="#fff" stroke-width="1.2"/>
      </svg>
    </div>
  </section>
</body>
</html>
```